Harbor Bean Corp Business Card Design

Harbor Bean Corp is a local owner and operator of several coffee shops in Irving, TX. Google "Brew Bright Corner" for an example of one of our shops.We would like an image that is professional, but with a slight nod to the protestant religious nature of our backers.The name "Harbor Bean" is a play on the concept of "rivers of living water". It also conveys the concept of a "brew of harbor". We desire to combine these concepts in the logo visualization, with the emphasis on the commercial side of the concept.

Target Market(s)

Upper class retail. No drive-through. Comfy lounges.

Industry/Entity Type

Coffee Shop

Contact Information for Business Card

Dale Mercer
Chief Operating Officer
Harbor Bean Corp
(832) 555 0147
dale@harborbean.example (address not yet active)

Requirements
Must have
• We do not have a logo yet. Need that as a part of the design.
• This needs to be original artwork. I need to own the art when the design is finished. I will look at submissions with stock artwork, but be advised that I will not accept the submission until original work is presented.

```html
<!DOCTYPE html>
<html lang="en">
<head>
<meta charset="utf-8">
<title>Harbor Bean Corp – Business Card Design</title>
<link href="https://fonts.googleapis.com/css2?family=Abel&family=Oswald:wght@500&family=Source+Sans+3:wght@400&display=swap" rel="stylesheet">
<style>
  :root {
    --board-bg: #e3dedb;
    --board-glow: #f4f2f0;
    --card-light: #f7f7f7;
    --card-mid: #e6e6e6;
    --card-edge: #4a4a4a;
    --brand-purple: #6a3f98;
    --label-purple: #6b5294;
    --coffee-brown: #6b3a1f;
    --ink: #1d1d1d;
    --divider: #cfcfcf;
    --leader: #3a3a3a;
    --photo-warm: #7a5a3e;
    --photo-light: #c9b79c;
  }
  * { box-sizing: border-box; margin: 0; padding: 0; }
  html, body { width: 1200px; height: 1200px; overflow: hidden; }
  body {
    background: radial-gradient(ellipse at 50% 48%, var(--board-glow) 0%, var(--board-bg) 70%);
    position: relative;
    font-family: "Abel", sans-serif;
  }
  .side-label {
    position: absolute;
    top: 164px;
    width: 300px;
    text-align: center;
    font-family: "Source Sans 3", sans-serif;
    font-size: 35px;
    color: var(--label-purple);
  }
  .side-label--front { left: 136px; }
  .side-label--back { left: 744px; }

  .card {
    position: absolute;
    border: 1px solid var(--card-edge);
    background: radial-gradient(ellipse at 55% 25%, var(--card-light) 0%, var(--card-mid) 85%);
    box-shadow: 3px 3px 5px rgba(0,0,0,0.35);
    overflow: hidden;
  }
  .card--front-a { left: 20px; top: 226px; width: 559px; height: 320px; }
  .card--back-a  { left: 612px; top: 226px; width: 553px; height: 316px; }
  .card--front-b { left: 18px; top: 616px; width: 562px; height: 321px; }
  .card--back-b  { left: 612px; top: 614px; width: 562px; height: 321px; }

  .card__band {
    position: absolute; left: 0; right: 0; bottom: 0; height: 13px;
    background: var(--coffee-brown);
  }
  .brand-dot {
    position: absolute;
    border-radius: 50%;
    background: var(--brand-purple);
  }
  .brand-name {
    position: absolute;
    text-align: center;
    font-family: "Oswald", sans-serif;
    font-weight: 500;
    font-variant: small-caps;
    color: var(--brand-purple);
    white-space: nowrap;
    line-height: 1;
  }
  .card__divider {
    position: absolute; left: 267px; top: 85px; width: 2px; height: 150px;
    background: var(--divider);
  }
  .contact {
    position: absolute; left: 335px; top: 100px;
    color: var(--ink);
    font-size: 17px;
    line-height: 22px;
  }
  .contact__name {
    font-family: "Oswald", sans-serif;
    font-weight: 500;
    font-variant: small-caps;
    font-size: 20px;
    color: var(--coffee-brown);
    line-height: 24px;
  }
  .tagline {
    position: absolute; left: 0; right: 0; top: 248px;
    text-align: center;
    font-size: 17px;
    letter-spacing: 11px;
    padding-left: 11px;
    color: var(--ink);
  }
  .shop-photo {
    position: absolute; left: 0; right: 0; bottom: 0; height: 108px;
    background: linear-gradient(90deg, var(--photo-light) 0%, var(--photo-warm) 35%, var(--photo-light) 60%, var(--photo-warm) 100%);
  }
  .leaders { position: absolute; left: 0; top: 0; }
  .callout {
    position: absolute;
    font-family: "Source Sans 3", sans-serif;
    font-size: 33px;
    white-space: nowrap;
    line-height: 1;
  }
  .callout--handle { left: 436px; top: 948px; color: var(--ink); }
  .callout--cup { left: 76px; top: 990px; color: var(--coffee-brown); }
  .callout--matt { left: 76px; top: 1034px; color: var(--label-purple); }
</style>
</head>
<body>
  <div class="side-label side-label--front">Front</div>
  <div class="side-label side-label--back">Back</div>

  <section class="card card--front-a">
    <div class="brand-dot" style="left:67px; top:85px; width:106px; height:106px;"></div>
    <div class="brand-name" style="left:0; width:240px; top:205px; font-size:31px;">Harbor Bean</div>
    <div class="card__divider"></div>
    <div class="contact">
      <div class="contact__name">Dale Mercer</div>
      <div>Chief Operating Officer</div>
      <div>Harbor Bean Corp</div>
      <div>(832) 555 0147</div>
      <div>dale@harborbean.example</div>
    </div>
    <div class="card__band"></div>
  </section>

  <section class="card card--back-a">
    <div class="brand-dot" style="left:210px; top:44px; width:132px; height:132px;"></div>
    <div class="brand-name" style="left:0; right:0; top:197px; font-size:37px;">Harbor Bean</div>
    <div class="tagline">brew of harbor</div>
  </section>

  <section class="card card--front-b">
    <div class="brand-dot" style="left:67px; top:85px; width:106px; height:106px;"></div>
    <div class="brand-name" style="left:0; width:240px; top:205px; font-size:31px;">Harbor Bean</div>
    <div class="card__divider"></div>
    <div class="contact">
      <div class="contact__name">Dale Mercer</div>
      <div>Chief Operating Officer</div>
      <div>Harbor Bean Corp</div>
      <div>(832) 555 0147</div>
      <div>dale@harborbean.example</div>
    </div>
    <div class="card__band"></div>
  </section>

  <section class="card card--back-b">
    <div class="brand-dot" style="left:226px; top:32px; width:108px; height:108px;"></div>
    <div class="brand-name" style="left:0; right:0; top:152px; font-size:31px;">Harbor Bean</div>
    <div class="shop-photo" role="img" aria-label="Photo of the coffee shop counter with pastry case, brewers and shelves of merchandise"></div>
  </section>

  <svg class="leaders" width="1200" height="1200" viewBox="0 0 1200 1200" aria-hidden="true">
    <g fill="none" stroke="var(--leader)" stroke-width="1">
      <polyline points="180,721 256,721 256,968 432,968"/>
      <polyline points="86,770 42,770 42,1009 74,1009"/>
      <polyline points="86,755 29,755 29,1052 74,1052"/>
    </g>
  </svg>
  <div class="callout callout--handle">Cup handle</div>
  <div class="callout callout--cup">Coffee cup with coffee</div>
  <div class="callout callout--matt">Coffee cup matt</div>
</body>
</html>
```